lanternox munchies snack packaging

We are a new startup snack company that need a design for a snack packaging. Our snack goes by the name of lanternox munchies. Its a traditional snack usually eaten during festive seasons in south east asia region. The idea is to revolutionize the notion of the snack from one that is eaten during these celebratory seasons to an everyday one. The packaging design should be modern and minimalist yet fun too, also taking into consideration that it should not appear to be too childish. It should stand out from the other snacks products like potato chips etc if placed on the same shelf. The colour scheme is not decided yet as we are open to more ideas but colours should be complementary and not more than 2 or 3 hopefully. There should be also be an enthic sense of south east asian features on the design and it should reflects the Chinese, Malay and indian heritage. It need not be too obvious, a subtle kind should suffice. The packaging should also have the particular graphic/shape of the mould that i have upload followed by the picture of the snack. I have included a mock up of the logo of my company. Proposed designs can feel free to alter the lanternox graphic to a more modern, minimalist yet whimsical and fun. Proposed designs should have a front and back view of the packaging. We are looking to launch at 4 to 5 flavours like white sesame, black sesame, peanuts with white sesame and original.
Updates

Project Deadline Extended
Reason: Not enough submissions coming in yet.

Project Deadline Extended
Reason: Extension of deadline to allow more designs to come in.

Target Market(s)

All ages from as young as 5 to 6 years old to 60 to 70s.

Industry/Entity Type

It Company

Font styles to use
Other font styles liked:
• Fonts should be simple and minimalist. Easy for elderly to read without straining the eyes.

Requirements
Must have
• My logo which I have designed. Designers can feel free to tweak and enhance the design of the logo. The colour is not definite yet. Consumers must know what
• we are selling from the design of the packaging without guessing how it look
• like. The suggested packaging dimension is 17cm (W) by 23.5cm (H).
Nice to have
• We are looking to print the package using kraft paper which I have attached.
Should not have
• religious inclination of motifs, logo etc.

```html
<!DOCTYPE html>
<html lang="en">
<head>
<meta charset="utf-8">
<title>lanternox munchies – snack pouch range</title>
<link href="https://fonts.googleapis.com/css2?family=Dancing+Script:wght@700&family=Questrial&family=Arimo:wght@400;700&display=swap" rel="stylesheet">
<style>
  :root {
    --backdrop: #8fd9dd;
    --brand-grey: #545454;
    --kraft: #d8a878;
    --kraft-dark: #c9956a;
    --pouch-white: #ebebeb;
    --pouch-black: #1d1d1d;
    --pouch-blue: #1f2b8e;
    --ink-red: #ad1a1e;
    --ink-white: #f4f4f4;
    --snack-light: #f3b640;
    --snack-deep: #c7781a;
  }
  * { margin: 0; padding: 0; box-sizing: border-box; }
  html, body { width: 1200px; height: 1000px; overflow: hidden; }
  body {
    position: relative;
    background: var(--backdrop);
    font-family: "Questrial", sans-serif;
  }
  .brand-mark {
    position: absolute;
    left: 0; top: 90px; width: 1200px;
    display: flex; flex-direction: column; align-items: center;
  }
  .brand-mark__circle {
    width: 116px; height: 116px;
    border: 3px solid var(--brand-grey);
    border-radius: 50%;
  }
  .brand-mark__name {
    margin-top: 4px;
    font-size: 21px;
    color: var(--brand-grey);
    letter-spacing: 0.5px;
  }
  .pouch {
    position: absolute;
    top: 320px;
    width: 306px; height: 450px;
    border-radius: 6px 6px 10px 10px;
    overflow: hidden;
  }
  .pouch--white { left: 67px; background: var(--pouch-white); --ink: var(--ink-red); }
  .pouch--black { left: 449px; background: var(--pouch-black); --ink: var(--ink-white); }
  .pouch--blue  { left: 825px; background: var(--pouch-blue); --ink: var(--ink-white); }
  .pouch__kraft { position: absolute; inset: 0; }
  .pouch__logo {
    position: absolute; left: 0; top: 36px; width: 226px;
    display: flex; flex-direction: column; align-items: center;
  }
  .pouch__logo-circle {
    width: 56px; height: 56px;
    border: 2px solid var(--ink);
    border-radius: 50%;
  }
  .pouch__logo-name {
    margin-top: 5px;
    font-size: 13px;
    color: var(--ink);
  }
  .pouch__title {
    position: absolute; left: 0; top: 186px; width: 226px;
    text-align: center;
    color: var(--ink);
  }
  .pouch__snacks {
    font-family: "Dancing Script", cursive;
    font-size: 54px; line-height: 1;
  }
  .pouch__flavour {
    font-size: 20px; line-height: 1.1;
  }
  .pouch__snack-photo { position: absolute; left: 185px; top: 280px; }
  .pouch__weight {
    position: absolute; left: 44px; top: 400px;
    font-family: "Arimo", sans-serif;
    color: var(--ink);
    line-height: 1.1;
  }
  .pouch--white .pouch__weight { color: var(--ink-red); }
  .pouch__weight-label { font-size: 10px; }
  .pouch__weight-value { font-size: 12px; font-weight: 700; }
</style>
</head>
<body>
  <div class="brand-mark">
    <div class="brand-mark__circle"></div>
    <div class="brand-mark__name">lanternox</div>
  </div>

  <div class="pouch pouch--white">
    <svg class="pouch__kraft" width="306" height="450" role="img" aria-label="Kraft paper panel with a repeating floral pattern">
      <polygon points="168,0 306,0 306,450 226,450" fill="var(--kraft)"/>
    </svg>
    <div class="pouch__logo"><div class="pouch__logo-circle"></div><div class="pouch__logo-name">lanternox</div></div>
    <div class="pouch__title"><div class="pouch__snacks">Snacks</div><div class="pouch__flavour">white sesame</div></div>
    <svg class="pouch__snack-photo" width="120" height="130" role="img" aria-label="Photo of two golden fried lattice snacks">
      <defs><radialGradient id="snack-a" cx="45%" cy="45%" r="60%"><stop offset="0" stop-color="var(--snack-light)"/><stop offset="1" stop-color="var(--snack-deep)"/></radialGradient></defs>
      <ellipse cx="75" cy="45" rx="42" ry="38" fill="url(#snack-a)"/>
      <ellipse cx="50" cy="85" rx="46" ry="40" fill="url(#snack-a)"/>
    </svg>
    <div class="pouch__weight"><div class="pouch__weight-label">net weight:</div><div class="pouch__weight-value">70 grams</div></div>
  </div>

  <div class="pouch pouch--black">
    <svg class="pouch__kraft" width="306" height="450" role="img" aria-label="Kraft paper panel with a repeating floral pattern">
      <polygon points="168,0 306,0 306,450 226,450" fill="var(--kraft)"/>
    </svg>
    <div class="pouch__logo"><div class="pouch__logo-circle"></div><div class="pouch__logo-name">lanternox</div></div>
    <div class="pouch__title"><div class="pouch__snacks">Snacks</div><div class="pouch__flavour">black sesame</div></div>
    <svg class="pouch__snack-photo" width="120" height="130" role="img" aria-label="Photo of two golden fried lattice snacks">
      <defs><radialGradient id="snack-b" cx="45%" cy="45%" r="60%"><stop offset="0" stop-color="var(--snack-light)"/><stop offset="1" stop-color="var(--snack-deep)"/></radialGradient></defs>
      <ellipse cx="75" cy="45" rx="42" ry="38" fill="url(#snack-b)"/>
      <ellipse cx="50" cy="85" rx="46" ry="40" fill="url(#snack-b)"/>
    </svg>
    <div class="pouch__weight"><div class="pouch__weight-label">net weight:</div><div class="pouch__weight-value">70 grams</div></div>
  </div>

  <div class="pouch pouch--blue">
    <svg class="pouch__kraft" width="306" height="450" role="img" aria-label="Kraft paper panel with a repeating floral pattern">
      <polygon points="168,0 306,0 306,450 226,450" fill="var(--kraft)"/>
    </svg>
    <div class="pouch__logo"><div class="pouch__logo-circle"></div><div class="pouch__logo-name">lanternox</div></div>
    <div class="pouch__title"><div class="pouch__snacks">Snacks</div><div class="pouch__flavour">peanuts with<br>white sesame</div></div>
    <svg class="pouch__snack-photo" width="120" height="130" role="img" aria-label="Photo of two golden fried lattice snacks">
      <defs><radialGradient id="snack-c" cx="45%" cy="45%" r="60%"><stop offset="0" stop-color="var(--snack-light)"/><stop offset="1" stop-color="var(--snack-deep)"/></radialGradient></defs>
      <ellipse cx="75" cy="45" rx="42" ry="38" fill="url(#snack-c)"/>
      <ellipse cx="50" cy="85" rx="46" ry="40" fill="url(#snack-c)"/>
    </svg>
    <div class="pouch__weight"><div class="pouch__weight-label">net weight:</div><div class="pouch__weight-value">70 grams</div></div>
  </div>
</body>
</html>
```